Building company with a modern and unique product looking for a business card to help us stand out

We currently have a logo but as our business has grown, we feel that our business card is not reflecting our modern and high quality product and help us stand out from the crowd. Our business is mainly in the construction of new homes using a unique method and materials that makes our homes fire proof, vermin and pest resistant and rated to the maximum cyclone category (category 5). We need a business card that helps us stand out as well as communicating professionalism, high quality and trustworthiness. I have attached our current logo with a black and white option, as well as our business card which is double sided. We would like to retain as much of the information that is currently on our business cards, but presented in a more sleek way. We do like our current colour palette ( white, black, yellow and grey) and have been looking primarily at business cards with a black background however we are open to other combinations of colour and layout as long as we stand out. Please feel free to tweak our logo to make it more suitable for a business card, we like the black option that we use but we have had trouble trying to get the white area to match the rest of the logo and blend effectively into a business card. Please do not hesitate to contact us with any questions as we really want this to be successful!

Target Market(s)

Large contracts including government and larger companies

Industry/Entity Type

Business

We will be providing this business card to potential clients including key government ministers and large funding companies, our business card should show that we are professional and reliable.

Requirements
Must have
• It must be easy to read and pleasing to the eye, It must contain as much of the information on the current business card and unless something really stands out, we will most likely pick a design that has all of the information included. It must include our logo of course and have some colour included.
Nice to have
• We are looking for a high end business card and would like to see designs that reflect this. We like the gloss/matte contrast, plastic cards with opaque/coloured areas and unique features not seen on everyday paper business cards. It would be nice to see a few different colour combinations, we are open to new ideas so please feel free to take some artistic licence.
Should not have
• Must not be too busy, difficult to read or be distracting from the information conveyed. Other than this please feel free to add your own touches and make it unique!

```html
<!DOCTYPE html>
<html lang="en">
<head>
<meta charset="utf-8">
<title>Corvale Building Company – Business Card</title>
<link rel="stylesheet" href="https://fonts.googleapis.com/css2?family=Lato:wght@300;400;700;900&display=swap">
<style>
  :root {
    --stage: #c9c9c9;
    --ink: #111111;
    --paper: #ffffff;
    --gold: #d3a92f;
    --rule: #8c8c8c;
    --text-light: #f2f2f2;
  }
  * { box-sizing: border-box; margin: 0; padding: 0; }
  html, body {
    width: 1200px; height: 900px; overflow: hidden;
    background: var(--stage);
    font-family: "Lato", sans-serif;
  }
  .canvas {
    position: relative; width: 1200px; height: 900px;
  }
  .card {
    position: absolute; left: 250px;
    width: 700px; height: 389px;
    background: var(--paper);
    box-shadow: 0 6px 18px rgba(0,0,0,0.25);
    overflow: hidden;
  }
  .card--front { top: 45px; }
  .card--back { top: 466px; }
  .card__shapes { position: absolute; inset: 0; width: 100%; height: 100%; }

  .brand {
    position: absolute; display: flex; align-items: center; gap: 10px;
    font-family: "Lato", sans-serif; font-weight: 700; color: var(--ink);
    line-height: 1.05;
  }
  .brand__mark { width: 16px; height: 16px; background: var(--gold); flex: none; }
  .card--front .brand { left: 62px; top: 78px; font-size: 26px; }
  .card--back .brand { left: 368px; top: 152px; font-size: 34px; }
  .card--back .brand__mark { width: 20px; height: 20px; }

  .contact {
    position: absolute; left: 445px; top: 128px;
    list-style: none; display: flex; flex-direction: column; gap: 20px;
    transform: rotate(-4deg); transform-origin: left top;
  }
  .contact__item {
    display: flex; align-items: center; gap: 14px;
    color: var(--text-light); font-size: 15px; letter-spacing: 0.3px;
  }
  .contact__item:nth-child(2) { margin-left: 12px; }
  .contact__item:nth-child(3) { margin-left: 24px; }
  .icon-ring {
    width: 22px; height: 22px; border: 1.5px solid var(--gold); border-radius: 50%;
    display: flex; align-items: center; justify-content: center; flex: none;
  }
  .icon-ring svg { width: 11px; height: 11px; }

  .person {
    position: absolute; left: 55px; top: 285px;
    display: flex; align-items: center; gap: 18px;
    transform: rotate(-4deg); transform-origin: left top;
  }
  .person__name {
    color: var(--text-light); font-size: 25px; font-weight: 900; letter-spacing: 1px;
    line-height: 1;
  }
  .person__name span { font-weight: 300; }
  .person__role {
    color: var(--text-light); font-size: 15px; font-weight: 400; letter-spacing: 0.6px;
    margin-top: 5px;
  }
  .person .icon-ring { width: 28px; height: 28px; }
  .person .icon-ring svg { width: 13px; height: 13px; }

  .abn {
    position: absolute; left: 42px; top: 160px;
    color: var(--text-light); font-size: 16px; letter-spacing: 0.8px;
    transform: rotate(22deg); transform-origin: left top;
  }
  .abn__label { color: var(--gold); font-weight: 700; }
</style>
</head>
<body>
<main class="canvas">

  <!-- Front side -->
  <section class="card card--front" aria-label="Business card, front">
    <svg class="card__shapes" viewBox="0 0 700 389" preserveAspectRatio="none" aria-hidden="true">
      <polygon points="270,0 700,0 455,75" fill="var(--gold)"/>
      <polygon points="0,270 455,75 700,118 700,389 0,389" fill="var(--ink)"/>
      <polyline points="0,266 455,71 700,114" fill="none" stroke="var(--rule)" stroke-width="6"/>
      <polyline points="270,0 455,75 700,2" fill="none" stroke="var(--rule)" stroke-width="3"/>
      <rect x="0" y="55" width="24" height="95" fill="var(--ink)"/>
    </svg>

    <div class="brand">
      <span class="brand__mark"></span>
      <span>Corvale Building<br>Company</span>
    </div>

    <ul class="contact">
      <li class="contact__item">
        <span class="icon-ring"><svg viewBox="0 0 12 12"><rect x="3" y="0.8" width="6" height="10.4" rx="1" fill="none" stroke="var(--gold)" stroke-width="1.3"/></svg></span>
        0400 555 019
      </li>
      <li class="contact__item">
        <span class="icon-ring"><svg viewBox="0 0 12 12"><path d="M2.5 1 L4.5 1 L5.3 3.6 L4 4.6 Q5 7 7.4 8 L8.4 6.7 L11 7.5 L11 9.5 Q10.5 11 8.8 11 Q1 10 1 2.6 Q1 1 2.5 1 Z" fill="var(--gold)"/></svg></span>
        (02) 5550 1234
      </li>
      <li class="contact__item">
        <span class="icon-ring"><svg viewBox="0 0 12 12"><rect x="0.8" y="2.5" width="10.4" height="7.5" fill="none" stroke="var(--gold)" stroke-width="1.3"/><polyline points="0.8,2.5 6,6.8 11.2,2.5" fill="none" stroke="var(--gold)" stroke-width="1.3"/></svg></span>
        office@corvalebuild.com
      </li>
    </ul>

    <div class="person">
      <span class="icon-ring"><svg viewBox="0 0 12 12"><circle cx="6" cy="3.6" r="2.6" fill="var(--gold)"/><path d="M1 11.5 Q1 7 6 7 Q11 7 11 11.5 Z" fill="var(--gold)"/></svg></span>
      <div>
        <p class="person__name">DALTON <span>REEVE</span></p>
        <p class="person__role">MANAGING DIRECTOR</p>
      </div>
    </div>
  </section>

  <!-- Back side -->
  <section class="card card--back" aria-label="Business card, back">
    <svg class="card__shapes" viewBox="0 0 700 389" preserveAspectRatio="none" aria-hidden="true">
      <polygon points="0,0 700,0 700,95 0,48" fill="var(--gold)"/>
      <polyline points="0,50 700,98" fill="none" stroke="var(--rule)" stroke-width="5"/>
      <polygon points="0,62 700,389 0,389" fill="var(--ink)"/>
      <line x1="0" y1="58" x2="700" y2="385" stroke="var(--rule)" stroke-width="5"/>
      <rect x="676" y="150" width="24" height="95" fill="var(--ink)"/>
    </svg>

    <div class="brand">
      <span class="brand__mark"></span>
      <span>Corvale Building<br>Company</span>
    </div>

    <p class="abn"><span class="abn__label">ABN:</span> 12 345 678 901</p>
  </section>

</main>
</body>
</html>
```